Real Estate Business Cards

Looking for a clean, sharp and professional look for our Real Estate investment Fund that invests in Multi Family Apartment buildings.

Target Market(s)

Real Estate Fund

Industry/Entity Type

Real Estate

Contact Information for Business Card

Company Description: Real Estate Investment Fund
Company Name: RKW Holdings
Name: Marcus Olvane
Cell: (917) 482-0657
Email: marcus@rkwholdings-example.com
Website: www.rkwholdings-example.com
Address: 418, 9th Street, Brooklyn NY 11218

Colors

Designer to choose colors to be used in the design.

Requirements
Nice to have
• Colors to match logo

```html
<!DOCTYPE html>
<html lang="en">
<head>
<meta charset="utf-8">
<title>RKW Holdings – Business Cards</title>
<link rel="stylesheet" href="https://fonts.googleapis.com/css2?family=Tinos:wght@400;700&display=swap">
<style>
  :root {
    --brand-blue: #1a74b0;
    --ink-grey: #4a4a4a;
    --rule-grey: #555555;
    --paper: #ffffff;
    --stage: #e6e7e9;
  }
  * { box-sizing: border-box; margin: 0; padding: 0; }
  html, body { width: 1200px; height: 800px; overflow: hidden; }
  body {
    background: var(--stage);
    font-family: "Tinos", "Times New Roman", serif;
    position: relative;
  }
  .card {
    position: absolute;
    width: 520px;
    height: 297px;
    top: 252px;
    overflow: hidden;
    box-shadow: 0 6px 18px rgba(0,0,0,0.18);
  }
  /* Front */
  .card-front { left: 50px; background: var(--brand-blue); }
  .card-front .brand {
    position: absolute;
    left: 0; right: 0; top: 96px;
    display: flex; flex-direction: column; align-items: center; gap: 22px;
  }
  .card-front .brand-square {
    width: 54px; height: 54px;
    border: 5px solid var(--paper);
  }
  .card-front .brand-name {
    color: var(--paper);
    font-size: 36px;
    line-height: 1;
    letter-spacing: 1px;
    text-transform: uppercase;
  }
  /* Back */
  .card-back { left: 630px; background: var(--paper); }
  .card-back .brand {
    position: absolute;
    right: 34px; top: 20px;
    display: flex; flex-direction: column; align-items: flex-end; gap: 12px;
  }
  .card-back .brand-square {
    width: 46px; height: 46px;
    border: 5px solid var(--brand-blue);
    margin-right: 56px;
  }
  .card-back .brand-name {
    color: var(--brand-blue);
    font-size: 26px;
    line-height: 1;
    letter-spacing: 1px;
    text-transform: uppercase;
  }
  .divider {
    position: absolute;
    left: 34px; right: 30px; top: 138px;
    height: 1.5px;
    background: var(--rule-grey);
  }
  .holder-name {
    position: absolute;
    left: 34px; top: 110px;
    color: var(--brand-blue);
    font-weight: 700;
    font-size: 21px;
    line-height: 1;
    letter-spacing: 0.5px;
    text-transform: uppercase;
  }
  .contact-list {
    position: absolute;
    left: 40px; top: 152px;
    list-style: none;
    color: var(--ink-grey);
    font-size: 16px;
    line-height: 24px;
  }
  .contact-list li { display: flex; align-items: center; gap: 10px; }
  .contact-list svg { width: 14px; height: 14px; flex: none; }
  .address {
    position: absolute;
    right: 38px; top: 150px;
    text-align: right;
    color: var(--ink-grey);
    font-size: 15px;
    line-height: 20px;
    font-style: normal;
  }
  .footer-band {
    position: absolute;
    left: 0; bottom: 0;
    width: 520px; height: 60px;
  }
  .website {
    position: absolute;
    right: 24px; bottom: 11px;
    color: var(--paper);
    font-size: 15px;
    line-height: 18px;
    letter-spacing: 0.3px;
  }
</style>
</head>
<body>

<section class="card card-front" aria-label="Card front">
  <div class="brand">
    <div class="brand-square"></div>
    <div class="brand-name">RKW Holdings</div>
  </div>
</section>

<section class="card card-back" aria-label="Card back">
  <div class="brand">
    <div class="brand-square"></div>
    <div class="brand-name">RKW Holdings</div>
  </div>

  <h1 class="holder-name">Marcus Olvane</h1>
  <div class="divider"></div>

  <ul class="contact-list">
    <li>
      <svg viewBox="0 0 16 16" aria-hidden="true"><path fill="#1a74b0" d="M3.6 1.5l2.3 2.6-1.3 1.6c.9 1.9 2.3 3.3 4.2 4.2l1.6-1.3 2.6 2.3-1.2 2.3C7.2 13 2.9 8.7 1.2 3.1z"/></svg>
      <span>(917) 482-0657</span>
    </li>
    <li>
      <svg viewBox="0 0 16 16" aria-hidden="true"><rect x="1" y="3.5" width="14" height="9.5" fill="#1a74b0"/><path d="M1.5 4l6.5 5 6.5-5" fill="none" stroke="#fff" stroke-width="1.2"/></svg>
      <span>marcus@rkwholdings-example.com</span>
    </li>
  </ul>

  <address class="address">418, 9th Street<br>Brooklyn NY 11218</address>

  <svg class="footer-band" viewBox="0 0 520 60" aria-hidden="true">
    <path d="M0 38 L236 38 Q246 38 252 30 L257 23" fill="none" stroke="#4a4a4a" stroke-width="4"/>
    <path d="M0 48 L250 48 Q262 48 268 38 L274 28 Q280 20 294 20 L520 20 L520 60 L0 60 Z" fill="#1a74b0"/>
  </svg>
  <div class="website">www.rkwholdings-example.com</div>
</section>

</body>
</html>
```